Emerging Australian photographer

I'm based in Cunderdin, a small rural town in the Wheatbelt area of Western Australia. So its a good thing that I love to travel further afield both for pleasure and for work. To me that is one and the same thing in any event!

My desire is to take photos that make the viewers heart skip. I love taking photos of people doing the things they love or being with the people they love. For me, the joy of photography comes with capturing the 'moments between the moments'. I like candid photography best of all - like when the new husband is staring joyfully at his bride and at that minute is unaware of the photographer capturing the moment.

I am available for weddings, engagements, birthdays, special events, newborns, family or individual portraits. By the end of the year I will be accredited with the Coastal Guild of Image Artisans.

I need a card that stands out but is elegant and would sit well on the table at a wedding or be given out in the church grounds. Classy and a little bit sassy.

Target Market(s)

Consumers who are seeking photographic services, eg wedding guests who see me at work and make enquiries.

Industry/Entity Type

Church

Contact Information for Business Card

Tamsin Bexley Photography
Tamsin Bexley
0452 307 618
www.tamsinbexley.com.au
photos@tamsinbexley.com.au

Requirements
Must have
• Must fit with the theme in the watermarks, but be crisp and modern.
Nice to have
• However it's not essential to have the pink! Facebook and Twitter logos.
Should not have
• Old style fonts like times new roman.

```html
<!DOCTYPE html>
<html lang="en">
<head>
<meta charset="utf-8">
<title>Tamsin Bexley Photography – Business Card</title>
<link rel="stylesheet" href="https://fonts.googleapis.com/css2?family=Jost:wght@300;400&display=swap">
<style>
  :root {
    --page-bg: #ffffff;
    --card-bg: #ffffff;
    --ink-dark: #5e5e5e;
    --ink-light: #ababab;
    --accent-pink: #f2b3c6;
    --ornament-grey: #8a8a8a;
    --card-shadow: rgba(0, 0, 0, 0.16);
  }
  html, body {
    margin: 0;
    padding: 0;
    width: 1200px;
    height: 1200px;
    overflow: hidden;
    background: var(--page-bg);
  }
  .canvas {
    position: relative;
    width: 1200px;
    height: 1200px;
    font-family: "Jost", "Helvetica Neue", Arial, sans-serif;
  }
  .card {
    position: absolute;
    width: 693px;
    height: 428px;
    background: var(--card-bg);
    box-shadow: 6px 8px 18px var(--card-shadow);
  }
  .card--front { left: 250px; top: 140px; }
  .card--back  { left: 256px; top: 636px; }

  /* Front */
  .brand {
    position: absolute;
    left: 0;
    right: 0;
    top: 200px;
    display: flex;
    justify-content: center;
    align-items: center;
    gap: 14px;
  }
  .brand__dot {
    width: 14px;
    height: 14px;
    border-radius: 50%;
    background: var(--accent-pink);
  }
  .brand__name {
    font-weight: 400;
    font-size: 38px;
    letter-spacing: 1px;
    color: var(--ink-dark);
  }
  .front__web {
    position: absolute;
    left: 0;
    right: 0;
    top: 366px;
    text-align: center;
    font-weight: 300;
    font-size: 22px;
    letter-spacing: 1.5px;
    color: var(--ink-light);
  }

  /* Back */
  .contact {
    position: absolute;
    left: 0;
    right: 0;
    text-align: center;
    font-weight: 300;
    color: var(--ink-light);
    letter-spacing: 1.5px;
  }
  .contact--name  { top: 96px;  font-size: 24px; }
  .contact--phone { top: 222px; font-size: 24px; }
  .contact--email { top: 310px; font-size: 22px; }
  .divider-ornament {
    position: absolute;
    left: 50%;
    top: 170px;
    width: 130px;
    height: 14px;
    margin-left: -65px;
    border-radius: 7px;
    background: linear-gradient(90deg, rgba(138,138,138,0.15), rgba(138,138,138,0.35), rgba(138,138,138,0.15));
  }
</style>
</head>
<body>
  <main class="canvas">
    <section class="card card--front">
      <div class="brand">
        <span class="brand__dot"></span>
        <span class="brand__name">Tamsin Bexley Photography</span>
      </div>
      <p class="front__web" style="margin:0">www.tamsinbexley.com.au</p>
    </section>

    <section class="card card--back">
      <p class="contact contact--name" style="margin:0">Tamsin Bexley</p>
      <div class="divider-ornament" role="img" aria-label="Decorative swirl divider"></div>
      <p class="contact contact--phone" style="margin:0">0452 307 618</p>
      <p class="contact contact--email" style="margin:0">photos@tamsinbexley.com.au</p>
    </section>
  </main>
</body>
</html>
```